Harrowby Wine Label - Design a front and smaller back label for an exclusive red wine

Harrowby Wines produces a very high quality, high priced wine from an old and prestigous vineyard in one of Australia's oldest, but smallest wine growing regions. The grapevines are old (like old men with gnarled arms and trunks) and they produce fewer grapes than younger vines but the grape quality (and thus wine quality) is magnificent and highly sought after as it produces wine of exceptional quality.
The vineyard was purchased by the Harrowby family in February 2010 from a multinational wine company who made wonderful, trophy winning wines for 10 years before the vineyard went into a decline.
The challenge is to produce 2 labels - a simple main front label that focuses on the Harrowby brand and a smaller, information rich, back label that relates the history of the vineyard.
The labels should have a white or charcoal grey background and impart tradition, quality, exclusivity and a little self indulgence which is why we want the family crest incorporated - the choice of font will help.
It might also impart a sense of fun so that it appeals to the 25-35 year old age bracket.
The label should be kept clean and simple not loud and busy. Preferred colours are black, grey and white. Red is fine if used sparingly

Here are the details:_

Front Label (115 long x 65-90mm wide)

Harrowby
Lanternwatch Reserve
2011
Mudgee
Wine of Australia 750ml

Back Label (dimensions to suit text and front label design; font size small; text in black so that it is readable in less than optimal light (eg candlelight at a restaurant table).

Harrowby
Lanternwatch Reserve 2011

This is the first release of The Lanternwatch’s Reserve – just 100 dozen bottles were made. The wine was made from Shiraz and 10% Cabernet Sauvignon grapes sourced from an iconic Mudgee vineyard that was established 1966 by Peter Vallis. In 1994, the vineyard known as ”Silver Hollow”, became the source of a decade of formidable, trophy winning wines under Tindalberg’s and later Quellwood’s ownership. The 20ha vineyard was purchased by Corin & Margaret Harrowby in 2010. The Silver Hollow name was retained by Quellwoods; no wine has been released under this label since the 2006 vintage.

The shaky old Shiraz vines are slowly being restored to full health using careful cane pruning techniques that stimulates fresh, new tissue growth, more even bunch sizes and better grape quality and consistency. The Shiraz grapes used in this wine were hand-picked from two rows of the first crop from the 46 year old, cane pruned vines. The 2011 Reserve is the first step to re-establish the traditions of a famous vineyard and one of Australia’s most sought after export wines.

“Deep and intense purple hues with aromas of ripe blackberry fruits, spice and eucalypt with rich chocolate complemented by subtle oak overtones. A rich and full bodied wine exhibiting a soft yet generous palate with plum, forest fruits and mint chocolate notes. A fine grained tannin structure displaying integrated oak characters adds to the complexity of the wine. This wine was aged for 18 months in a blend of new French oak hogsheads and one year old American hogsheads, crafting a blend with great structure and length of flavour which will develop into a Mudgee classic” – Lewis Farrant, Winemaker

13.5% Alc/Vol.
Contains approx 8.0 std drinks
Preservative (220) added

Harrowby Wines
Tallowbend Rd, Mudgee 2850
www.harrowbywines.example.au

Reason: My apologies to the designers who have kindly submitted some wonderful designs. I am trying to achieve a conscentious between shareholders. This is difficult as they are in different parts of the world and I have learned through this experience that opinions on wine labels are quite diverse!!! The feedback I have received so far indicates the following (1) A light or white background is preferred (2) The crest should not be a dominant part of the label (3) The label needs to be clean, fresh and uncomplicated (4) If red is used it should be in minor detail only (5) "Harrowby" should be distinctive. The font is difficult for us! (6) We are considering "The Lanternwatch" RESERVE instead of "Lanternwatch's" RESERVE (7) The text on the back label is too long; I will edit and re-upload Many thanks for your help and patience Kind regards Corin

Good Morning All,
I have edited the back label text to reduce the size of the label. A Word file with the changes has just been uploaded.
Cheers
Corin

Dear Designers,
Thank you all so very much for the wonderful selection of designs you have submitted my family have all been overwhelmed by the quality and skill level exhibited and we all appreciate you your efforts
Kindest regards
Corin

Target Market(s)

25-35 year old men and women of Australia, China, US & UK

Industry/Entity Type

Restaurant

Requirements
Must have
• Crest
Should not have
• Animals on the label

```html
<!DOCTYPE html>
<html lang="en">
<head>
<meta charset="utf-8">
<title>Harrowby Wine Label – The Lanternwatch's Reserve 2011</title>
<link href="https://fonts.googleapis.com/css2?family=Cinzel:wght@400;600&family=Cormorant+SC:wght@500;600&display=swap" rel="stylesheet">
<style>
  :root {
    --backdrop: #e4e4e4;
    --label-light: #f5f5f3;
    --label-shade: #e3e3e0;
    --ink: #1a1a1a;
    --ink-soft: #3a3a3a;
    --rule-grey: #8a8a8a;
    --mark-grey: #6e6e6e;
    --accent-red: #d9221d;
    --crest-tone: #c9c9c6;
  }
  * { box-sizing: border-box; margin: 0; padding: 0; }
  html, body {
    width: 1200px; height: 900px; overflow: hidden;
    background: var(--backdrop);
  }
  .label-set { position: relative; width: 1200px; height: 900px; }

  .label {
    position: absolute; top: 265px; width: 237px; height: 446px;
    background: linear-gradient(160deg, var(--label-light), var(--label-shade));
    box-shadow: 0 1px 3px rgba(0,0,0,.18);
    color: var(--ink);
    text-align: center;
  }
  .label--front-grey { left: 63px; }
  .label--back-grey  { left: 345px; }
  .label--front-red  { left: 627px; }
  .label--back-red   { left: 908px; }

  /* Front label */
  .crest {
    position: absolute; left: 96px; top: 22px; width: 44px; height: 60px;
    background: linear-gradient(180deg, var(--crest-tone), #b5b5b2);
    border-radius: 3px 3px 22px 22px;
  }
  .brand-name {
    position: absolute; left: 0; right: 0; top: 140px;
    font-family: "Cinzel", serif; font-weight: 400;
    font-size: 40px; letter-spacing: 1px; color: var(--ink);
  }
  .gate-mark {
    position: absolute; left: 99px; top: 273px; width: 38px; height: 16px;
    background: var(--mark-grey);
  }
  .label--front-red .gate-mark { background: var(--accent-red); }
  .reserve-title {
    position: absolute; left: 0; right: 0; top: 305px;
    font-family: "Cinzel", serif; font-size: 11.5px; letter-spacing: .8px;
    color: var(--ink-soft);
  }
  .vintage {
    position: absolute; left: 0; right: 0; top: 324px;
    font-family: "Cinzel", serif; font-size: 14px; letter-spacing: 1.5px;
    color: var(--ink-soft);
  }
  .divider {
    position: absolute; left: 50px; right: 50px; height: 6px;
    display: flex; align-items: center; gap: 8px;
  }
  .divider::before, .divider::after {
    content: ""; flex: 1; height: 1px; background: var(--rule-grey);
  }
  .divider i {
    width: 5px; height: 5px; background: var(--mark-grey); transform: rotate(45deg);
  }
  .label--front-red .divider::before, .label--front-red .divider::after,
  .label--back-red .divider::before, .label--back-red .divider::after { background: var(--accent-red); }
  .label--front-red .divider i, .label--back-red .divider i { background: var(--accent-red); }
  .label .divider--front { top: 363px; }
  .region {
    position: absolute; left: 0; right: 0; top: 391px;
    font-family: "Cinzel", serif; font-size: 12px; letter-spacing: 1px;
  }
  .origin {
    position: absolute; left: 0; right: 0; top: 409px;
    font-family: "Cinzel", serif; font-size: 7px; letter-spacing: 1.6px; color: var(--ink-soft);
  }
  .volume {
    position: absolute; left: 0; right: 0; top: 419px;
    font-family: "Cinzel", serif; font-size: 11px; letter-spacing: .5px;
  }

  /* Back label */
  .brand-name--small {
    position: absolute; left: 120px; top: 26px;
    font-family: "Cinzel", serif; font-size: 13px; letter-spacing: .5px;
  }
  .back-title {
    position: absolute; left: 0; right: 0; top: 48px;
    font-family: "Cinzel", serif; font-weight: 600; font-size: 7.5px; letter-spacing: .3px;
  }
  .story {
    position: absolute; left: 20px; right: 20px; top: 64px;
    font-family: "Cormorant SC", serif; font-weight: 600;
    font-size: 6.4px; line-height: 8.6px; text-align: justify;
    color: var(--ink);
  }
  .story p + p { margin-top: 8px; }
  .story .credit { font-size: 5px; }
  .label .divider--back { top: 330px; left: 60px; right: 60px; }
  .label--back-grey .divider--back::before, .label--back-grey .divider--back::after { background: #b8b8b8; }
  .facts {
    position: absolute; left: 0; right: 0; top: 354px;
    font-family: "Cormorant SC", serif; font-weight: 600; line-height: 10px;
  }
  .facts .alc { font-size: 9px; }
  .facts .std, .facts .pres { font-size: 7px; }
  .producer {
    position: absolute; left: 0; right: 0; top: 391px;
    font-family: "Cormorant SC", serif; font-weight: 600; line-height: 10px;
  }
  .producer .name { font-size: 8px; }
  .producer .address { font-size: 6.5px; letter-spacing: .5px; }
  .web {
    position: absolute; left: 0; right: 0; top: 420px;
    font-family: "Cormorant SC", serif; font-weight: 600; font-size: 6.8px;
    letter-spacing: .8px; text-decoration: underline;
  }
</style>
</head>
<body>
<main class="label-set">

  <section class="label label--front-grey" aria-label="Front label, grey accent">
    <div class="crest" role="img" aria-label="Harrowby family crest"></div>
    <h1 class="brand-name">Harrowby</h1>
    <div class="gate-mark" role="img" aria-label="Gate emblem"></div>
    <p class="reserve-title">The Lanternwatch's Reserve</p>
    <p class="vintage">2011</p>
    <div class="divider divider--front"><i></i></div>
    <p class="region">Mudgee</p>
    <p class="origin">Wine of Australia</p>
    <p class="volume">750mL</p>
  </section>

  <section class="label label--back-grey" aria-label="Back label, grey accent">
    <p class="brand-name--small">Harrowby</p>
    <h2 class="back-title">The Lanternwatch's Reserve 2011</h2>
    <div class="story">
      <p>The Shiraz and Cabernet grapes from which this wine was made were handpicked from a 20ha vineyard that was established in 1966. The vineyard formerly known as “Silver Hollow” was purchased by the Harrowby family in 2010.</p>
      <p>The shaky old Shiraz vines are slowly being restored to full health using careful cane pruning techniques to achieve better grape quality and consistency. The 2011 Reserve is the first step to re-establish the traditions of a famous vineyard and one of Australia's most sought after export wines.</p>
      <p>“Deep and intense purple hues with aromas of ripe blackberry fruits, spice and eucalypt with rich chocolate complemented by subtle oak overtones. A rich and full bodied wine exhibiting a soft yet generous palate with plum, forest fruits and mint chocolate notes. A fine grained tannin structure displaying integrated oak characters adds to the complexity of the wine. This wine was aged for 18 months in a blend of new French oak hogsheads and one year old American hogsheads, crafting a blend with great structure and length of flavour which will develop into a Mudgee classic.” <span class="credit">– Lewis Farrant, Winemaker</span></p>
    </div>
    <div class="divider divider--back"><i></i></div>
    <div class="facts">
      <p class="alc">13.5% Alc/Vol.</p>
      <p class="std">Contains approx 8.0 std drinks</p>
      <p class="pres">Preservative (220) added</p>
    </div>
    <div class="producer">
      <p class="name">Harrowby Wines</p>
      <p class="address">Tallowbend Rd, Mudgee 2850</p>
    </div>
    <p class="web">www.harrowbywines.example.au</p>
  </section>

  <section class="label label--front-red" aria-label="Front label, red accent">
    <div class="crest" role="img" aria-label="Harrowby family crest"></div>
    <h1 class="brand-name">Harrowby</h1>
    <div class="gate-mark" role="img" aria-label="Gate emblem in red"></div>
    <p class="reserve-title">The Lanternwatch's Reserve</p>
    <p class="vintage">2011</p>
    <div class="divider divider--front"><i></i></div>
    <p class="region">Mudgee</p>
    <p class="origin">Wine of Australia</p>
    <p class="volume">750mL</p>
  </section>

  <section class="label label--back-red" aria-label="Back label, red accent">
    <p class="brand-name--small">Harrowby</p>
    <h2 class="back-title">The Lanternwatch's Reserve 2011</h2>
    <div class="story">
      <p>The Shiraz and Cabernet grapes from which this wine was made were handpicked from a 20ha vineyard that was established in 1966. The vineyard formerly known as “Silver Hollow” was purchased by the Harrowby family in 2010.</p>
      <p>The shaky old Shiraz vines are slowly being restored to full health using careful cane pruning techniques to achieve better grape quality and consistency. The 2011 Reserve is the first step to re-establish the traditions of a famous vineyard and one of Australia's most sought after export wines.</p>
      <p>“Deep and intense purple hues with aromas of ripe blackberry fruits, spice and eucalypt with rich chocolate complemented by subtle oak overtones. A rich and full bodied wine exhibiting a soft yet generous palate with plum, forest fruits and mint chocolate notes. A fine grained tannin structure displaying integrated oak characters adds to the complexity of the wine. This wine was aged for 18 months in a blend of new French oak hogsheads and one year old American hogsheads, crafting a blend with great structure and length of flavour which will develop into a Mudgee classic.” <span class="credit">– Lewis Farrant, Winemaker</span></p>
    </div>
    <div class="divider divider--back"><i></i></div>
    <div class="facts">
      <p class="alc">13.5% Alc/Vol.</p>
      <p class="std">Contains approx 8.0 std drinks</p>
      <p class="pres">Preservative (220) added</p>
    </div>
    <div class="producer">
      <p class="name">Harrowby Wines</p>
      <p class="address">Tallowbend Rd, Mudgee 2850</p>
    </div>
    <p class="web">www.harrowbywines.example.au</p>
  </section>

</main>
</body>
</html>
```